i need a template design for online store

hi great designers, i need a template for any online store. But preferably well owned shopping carts. I would be an added advantage if the store is setup for me. I need a mature and attractive colours. My online store deals in electronics.

Shopping

1 page

```html
<!DOCTYPE html>
<html lang="en">
<head>
<meta charset="utf-8">
<title>Voltmart</title>
<link href="https://fonts.googleapis.com/css2?family=Questrial&display=swap" rel="stylesheet">
<style>
  :root {
    --navy: #0d3a80;
    --bar: #d5d5d5;
    --bar-sub: #cbcbcb;
    --text-grey: #7a7a7a;
    --headline-grey: #8a8a8a;
    --body-grey: #9a9a9a;
    --price-red: #b3202c;
    --accent-orange: #e58a1c;
    --white: #ffffff;
  }
  * { box-sizing: border-box; margin: 0; padding: 0; }
  html, body {
    width: 1200px;
    height: 1123px;
    overflow: hidden;
    background: var(--white);
    font-family: "Questrial", sans-serif;
  }
  h1, h2, h3 { font-weight: 400; }
  .page { position: relative; width: 1200px; height: 1123px; }

  /* Hero */
  .hero {
    position: absolute; left: 0; top: 0; width: 1200px; height: 568px;
    background:
      radial-gradient(ellipse at 85% 40%, rgba(170,40,40,.55) 0%, rgba(170,40,40,0) 35%),
      radial-gradient(ellipse at 60% 10%, rgba(150,110,90,.5) 0%, rgba(150,110,90,0) 40%),
      radial-gradient(ellipse at 20% 45%, rgba(225,190,170,.7) 0%, rgba(225,190,170,0) 40%),
      linear-gradient(160deg, #c9d8e8 0%, #e4ebf2 40%, #d9d3cf 70%, #b9aea6 100%);
  }
  .promo-frame {
    position: absolute; left: 212px; top: 203px; width: 777px; height: 222px;
    border: 2px solid rgba(255,255,255,.9);
    background: rgba(255,255,255,.55);
    text-align: center;
  }
  .promo-title {
    margin-top: 28px;
    font-size: 52px; letter-spacing: 5px; color: var(--headline-grey);
    line-height: 60px; white-space: nowrap;
  }
  .promo-rule {
    width: 333px; height: 1px; background: #9a9a9a; margin: 9px auto 18px;
  }
  .promo-sub {
    font-size: 26px; letter-spacing: 2.6px; color: #7c7c7c; line-height: 40px;
  }
  .see-more {
    position: absolute; left: 522px; top: 441px; width: 154px; height: 44px;
    background: var(--navy); color: var(--white);
    font-size: 19px; letter-spacing: 1px;
    display: flex; align-items: center; justify-content: center;
  }

  /* Header */
  .header-bar {
    position: absolute; left: 0; top: 568px; width: 1200px; height: 83px;
    background: var(--bar); border-top: 2px solid #e8e8e8;
  }
  .brand {
    position: absolute; left: 90px; top: 22px;
    display: flex; align-items: center; gap: 10px;
    color: var(--navy); font-size: 34px; line-height: 38px; letter-spacing: 1px;
  }
  .brand-mark { width: 14px; height: 14px; background: var(--navy); }
  .main-nav a {
    position: absolute; top: 35px; font-size: 11px; letter-spacing: .5px;
    color: var(--text-grey); text-decoration: none;
  }
  .cart { position: absolute; left: 878px; top: 0; width: 322px; height: 83px; }
  .cart svg { position: absolute; left: 0; top: 0; }
  .cart-label {
    position: absolute; left: 110px; top: 18px; color: var(--white);
    font-size: 26px; line-height: 26px;
  }
  .cart-count {
    position: absolute; left: 110px; top: 45px; color: var(--white);
    font-size: 16px; letter-spacing: .5px;
  }
  .cart-count b { color: var(--accent-orange); font-weight: 400; margin-right: 6px; }

  .category-bar {
    position: absolute; left: 0; top: 651px; width: 1200px; height: 26px;
    background: var(--bar-sub);
  }
  .category-nav a {
    position: absolute; top: 7px; font-size: 11px; letter-spacing: .5px;
    color: var(--text-grey); text-decoration: none;
  }
  .search {
    position: absolute; left: 787px; top: 4px; width: 239px; height: 18px;
    background: var(--white); font-size: 10px; color: var(--text-grey);
    padding: 3px 4px;
  }

  /* Products */
  .section-title {
    position: absolute; left: 0; top: 722px; width: 1200px; text-align: center;
    font-size: 20px; letter-spacing: 2px; color: var(--navy);
  }
  .product { position: absolute; top: 790px; width: 182px; }
  .product-photo {
    margin-left: 26px; width: 134px; height: 132px;
    background: linear-gradient(90deg, #2a2d33 0%, #3c4a63 45%, #7a7c80 60%, #b9babc 100%);
    border-radius: 6px;
  }
  .product-name {
    margin-top: 18px; font-size: 16px; letter-spacing: 1.2px; color: var(--navy);
  }
  .product-desc {
    margin-top: 7px; font-size: 9.5px; line-height: 11.3px; color: var(--body-grey);
    text-align: justify;
  }
  .product-price { margin-top: 8px; }
  .price-old {
    font-size: 16px; color: #8a8a8a; text-decoration: line-through; margin-right: 4px;
  }
  .price-new { font-size: 22px; color: var(--price-red); }
</style>
</head>
<body>
<div class="page">

  <section class="hero" role="img" aria-label="Photo of hands holding and using smartphones at a café table">
  </section>
  <div class="promo-frame">
    <h1 class="promo-title">30% OFF THIS SUMMER</h1>
    <div class="promo-rule"></div>
    <p class="promo-sub">ALL SMARTPHONES IN OUR STORE<br>WITH UNBELIEVABLE PRICES</p>
  </div>
  <a class="see-more">SEE MORE</a>

  <header class="header-bar">
    <div class="brand">
      <span class="brand-mark"></span>
      <span class="brand-name">VOLTMART</span>
    </div>
    <nav class="main-nav">
      <a style="left:328px">ABOUT US</a>
      <a style="left:427px">NEWS</a>
      <a style="left:501px">SERVICES</a>
      <a style="left:578px">TODAY DEALS</a>
      <a style="left:690px">HELP</a>
      <a style="left:773px">SIGN IN</a>
    </nav>
    <div class="cart">
      <svg width="322" height="83" viewBox="0 0 322 83">
        <polygon points="32,0 322,0 322,83 32,83 0,41" fill="#0d3a80"/>
        <g fill="none" stroke="#ffffff" stroke-width="4" stroke-linejoin="round" stroke-linecap="round">
          <path d="M48 22 H58 L66 52 H94 L101 30 H62"/>
          <path d="M64 45 H96"/>
        </g>
        <circle cx="71" cy="60" r="4.5" fill="#ffffff"/>
        <circle cx="90" cy="60" r="4.5" fill="#ffffff"/>
      </svg>
      <div class="cart-label">CART</div>
      <div class="cart-count"><b>0</b>PRODUCTS</div>
    </div>
  </header>

  <div class="category-bar">
    <nav class="category-nav">
      <a style="left:172px">CELL PHONES</a>
      <a style="left:273px">COMPUTERS</a>
      <a style="left:363px">TV/VIDEO</a>
      <a style="left:435px">AUDIO</a>
      <a style="left:490px">CAMERAS</a>
      <a style="left:564px">CAR</a>
      <a style="left:608px">OFFICE</a>
      <a style="left:669px">MUSIC</a>
      <a style="left:725px">OTHERS</a>
    </nav>
    <div class="search">SEARCH</div>
  </div>

  <h2 class="section-title">WHAT’S NEW</h2>

  <article class="product" style="left:209px">
    <div class="product-photo" role="img" aria-label="Smartphone shown from front and back"></div>
    <h3 class="product-name">LOREM IPSUM</h3>
    <p class="product-desc">Lorem ipsum dolor sit amet, consectetur adipiscing elit. Nulla congue risus ut nisi placerat, sed rutrum lacus dignissim. Donec fringilla lectus a mauris iaculis, eu bibendum nulla vulputate. Duis rutrum metus nec ligula vulputate, vitae efficitur dolor faucibus.</p>
    <div class="product-price"><span class="price-old">$111.11</span><span class="price-new">$99.99</span></div>
  </article>

  <article class="product" style="left:409px">
    <div class="product-photo" role="img" aria-label="Smartphone shown from front and back"></div>
    <h3 class="product-name">LOREM IPSUM</h3>
    <p class="product-desc">Lorem ipsum dolor sit amet, consectetur adipiscing elit. Nulla congue risus ut nisi placerat, sed rutrum lacus dignissim. Donec fringilla lectus a mauris iaculis, eu bibendum nulla vulputate. Duis rutrum metus nec ligula vulputate, vitae efficitur dolor faucibus.</p>
    <div class="product-price"><span class="price-old">$111.11</span><span class="price-new">$99.99</span></div>
  </article>

  <article class="product" style="left:609px">
    <div class="product-photo" role="img" aria-label="Smartphone shown from front and back"></div>
    <h3 class="product-name">LOREM IPSUM</h3>
    <p class="product-desc">Lorem ipsum dolor sit amet, consectetur adipiscing elit. Nulla congue risus ut nisi placerat, sed rutrum lacus dignissim. Donec fringilla lectus a mauris iaculis, eu bibendum nulla vulputate. Duis rutrum metus nec ligula vulputate, vitae efficitur dolor faucibus.</p>
    <div class="product-price"><span class="price-old">$111.11</span><span class="price-new">$99.99</span></div>
  </article>

  <article class="product" style="left:809px">
    <div class="product-photo" role="img" aria-label="Smartphone shown from front and back"></div>
    <h3 class="product-name">LOREM IPSUM</h3>
    <p class="product-desc">Lorem ipsum dolor sit amet, consectetur adipiscing elit. Nulla congue risus ut nisi placerat, sed rutrum lacus dignissim. Donec fringilla lectus a mauris iaculis, eu bibendum nulla vulputate. Duis rutrum metus nec ligula vulputate, vitae efficitur dolor faucibus.</p>
    <div class="product-price"><span class="price-old">$111.11</span><span class="price-new">$99.99</span></div>
  </article>

</div>
</body>
</html>
```